Teilnehmerzertifikat für Expeditionsmobil
Zielgruppe
Wir bitten alles Rund um das Thema Expeditionsmobil an. Unter anderem unsere Lagerfeuer und Weite Fahrt nach Tunesien und dafür benötige ich ein Teilnehmer Zertifikat.
Aufgabenstellung
Im Hintergrund soll ein Bild von der Sahara verarbeitet sein und im Vordergrund möchte ich von jedem Teilnehmer ein Bild mit dem eigenen Expeditonsfahrzeug einfügen. Das Zertifikat soll persöhnlich und wie von einem Freund sein

```html
<!DOCTYPE html>
<html lang="de">
<head>
<meta charset="utf-8">
<title>Teilnehmerzertifikat – Lagerfeuer und Weite Fahrt Tunesien</title>
<link href="https://fonts.googleapis.com/css2?family=Bebas+Neue&family=Black+Ops+One&family=PT+Sans+Narrow:wght@700&display=swap" rel="stylesheet">
<style>
  :root {
    --paper: #ffffff;
    --sky-top: #6d9cc4;
    --sky-mid: #c9c7b9;
    --glow: #f2a83a;
    --sunset: #e4561c;
    --ember: #b8361a;
    --dune: #8a5a48;
    --dune-deep: #6b3f33;
    --ink-dark: #2a1a14;
    --text-light: #ffffff;
    --photo-dusk: #3d5f86;
    --photo-sand: #7b4b3c;
    --pin: #f0782a;
  }
  * { margin: 0; padding: 0; box-sizing: border-box; }
  html, body { width: 848px; height: 1200px; overflow: hidden; background: var(--paper); }
  .certificate {
    position: relative; width: 848px; height: 1200px; overflow: hidden;
    background: var(--paper);
    font-family: "PT Sans Narrow", "Arial Narrow", sans-serif;
  }
  .backdrop {
    position: absolute; left: 18px; top: 14px; width: 812px; height: 1150px;
    clip-path: polygon(0 2%, 3% 0, 20% 1%, 40% 0, 62% 1.2%, 80% 0, 97% 0.8%, 100% 3%,
      99% 25%, 100% 45%, 98.6% 60%, 100% 80%, 99% 97%, 96% 100%, 75% 99%, 50% 100%,
      25% 99.2%, 4% 100%, 0 97%, 1.2% 75%, 0 55%, 1% 35%, 0 15%);
    background: linear-gradient(180deg,
      var(--sky-top) 0%, var(--sky-mid) 16%, #d9b48a 26%, var(--glow) 34%,
      var(--sunset) 40%, var(--ember) 45%, var(--dune) 52%, #93624f 72%, var(--dune-deep) 100%);
  }
  .title {
    position: absolute; left: 340px; top: 74px; width: 470px;
    font-family: "Bebas Neue", "Oswald", sans-serif; color: var(--paper);
    line-height: 0.9; text-align: right;
  }
  .title__line { display: block; font-size: 60px; letter-spacing: 1px; }
  .title__country {
    display: inline-block; margin-top: 8px; padding: 4px 16px 0;
    border: 3px solid var(--paper); background: rgba(255,255,255,0.85);
    color: #b9b0a6; font-size: 42px; letter-spacing: 3px;
  }
  .watermark-word {
    position: absolute; left: 28px; top: 300px; width: 800px;
    font-family: "Black Ops One", "Impact", sans-serif; font-size: 150px;
    letter-spacing: 4px; color: rgba(255,255,255,0.45);
    transform: rotate(-3deg); text-align: center; line-height: 1;
  }
  .participant-name {
    position: absolute; left: 228px; top: 510px;
    font-family: "Black Ops One", "Impact", sans-serif; font-size: 38px;
    letter-spacing: 2px; color: var(--ink-dark);
  }
  .polaroid {
    position: absolute; left: 52px; top: 590px; width: 340px; height: 415px;
    background: var(--paper); padding: 22px 22px 60px;
    transform: rotate(-3deg); box-shadow: 0 6px 14px rgba(0,0,0,0.35);
  }
  .polaroid__photo {
    position: relative; width: 100%; height: 100%;
    background: linear-gradient(180deg, var(--photo-dusk) 0%, #8da4bf 35%, #e08a52 52%, var(--photo-sand) 62%, #5a342a 100%);
    display: flex; align-items: flex-end; justify-content: center; padding-bottom: 40px;
  }
  .polaroid__placeholder {
    font-family: "Black Ops One", "Impact", sans-serif; font-size: 34px; line-height: 1.05;
    color: var(--text-light); text-align: center; letter-spacing: 2px;
    text-shadow: 0 0 4px #000, 0 0 2px #000;
  }
  .pin { position: absolute; left: 212px; top: 538px; }
  .message {
    position: absolute; left: 478px; top: 612px; width: 320px;
    color: var(--text-light); font-size: 15.5px; line-height: 28px;
  }
  .signature-line {
    position: absolute; left: 482px; top: 982px; width: 290px; height: 1px;
    background: rgba(255,255,255,0.8);
  }
  .brand {
    position: absolute; left: 0; width: 848px; top: 1040px;
    display: flex; justify-content: center; align-items: center; gap: 12px;
    color: var(--text-light); font-size: 28px; letter-spacing: 2px; text-transform: uppercase;
  }
  .brand__dot { width: 16px; height: 16px; border-radius: 50%; background: var(--text-light); }
</style>
</head>
<body>
<main class="certificate">
  <div class="backdrop" role="img" aria-label="Foto: Sonnenuntergang über den Dünen der Sahara in Tunesien"></div>

  <h1 class="title">
    <span class="title__line">Lagerfeuer und</span>
    <span class="title__line">Weite Fahrt</span>
    <span class="title__country">Tunesien</span>
  </h1>

  <div class="watermark-word" aria-hidden="true">ZERTIFIKAT</div>

  <h2 class="participant-name">VORNAME NACHNAME</h2>

  <figure class="polaroid">
    <div class="polaroid__photo" role="img" aria-label="Teilnehmerfoto mit dem eigenen Expeditionsfahrzeug in der Wüste">
      <span class="polaroid__placeholder">DUMMY<br>FÜR BILD</span>
    </div>
  </figure>

  <svg class="pin" width="34" height="40" viewBox="0 0 34 40" aria-hidden="true">
    <line x1="17" y1="18" x2="19" y2="38" stroke="#9a9a9a" stroke-width="2"/>
    <circle cx="17" cy="14" r="12" fill="var(--pin)"/>
    <circle cx="13" cy="10" r="4" fill="#ffc08a"/>
  </svg>

  <p class="message">
    Ihr habt mit Begeisterung und Abenteuerlust an unserer gemeinsamen Reise durch Tunesien teilgenommen.
    Mit eurem Expeditionsmobil habt ihr die Wüste bezwungen, neue Freundschaften geschlossen und die Magie dieses einzigartigen Landes erlebt.
    Danke, dass ihr Teil dieser besonderen Tour wart – auf viele weitere Abenteuer!
  </p>

  <div class="signature-line"></div>

  <div class="brand">
    <span class="brand__dot"></span>
    <span class="brand__name">Kranichpfad Reisen</span>
  </div>
</main>
</body>
</html>
```